Prepare a modern, professional business card for Bramford Ledger Services (BLS) Our company is in the banking, compliance and finance industry. We provide kiosks, software integration, and compliance guidelines so that banks can "bank" Marijuana Dispensaries with TrevMon, Office of Halvern Affairs and NTRB approval.

Target Market(s)

Banks

Industry/Entity Type

Business

Contact Information for Business Card

Owen R Pelley
Bramford Ledger Services
Vice President
742 Quarry Ridge Road
Suite 310
Las Vegas, NV 89135
owen@bramfordls.net
702-555-0147

Font styles to use
Sans Serif

Requirements
Nice to have
• I like the clean simple appearance of Quillon computers. Perhaps the three LETTERS of BLS can be the LOGO on the Card and the Company name could be incorporated in the contact information. Like colors of white, black and gray

```html
<!DOCTYPE html>
<html lang="en">
<head>
<meta charset="utf-8">
<title>Bramford Ledger Services — Business Card</title>
<link href="https://fonts.googleapis.com/css2?family=Source+Sans+3:wght@300;400;600&display=swap" rel="stylesheet">
<style>
  :root {
    --backdrop: #333333;
    --card: #ffffff;
    --ink: #2b2b2b;
    --ink-soft: #3a3a3a;
  }
  * { margin: 0; padding: 0; box-sizing: border-box; }
  html, body {
    width: 1200px; height: 1200px; overflow: hidden;
    background: var(--backdrop);
    font-family: "Source Sans 3", sans-serif;
  }
  .card {
    position: absolute; left: 50px; top: 278px;
    width: 1100px; height: 644px;
    background: var(--card);
    color: var(--ink);
  }
  .card__name {
    position: absolute; left: 82px; top: 52px;
    font-size: 82px; font-weight: 300; letter-spacing: 1px;
    line-height: 1; white-space: nowrap;
  }
  .card__title {
    position: absolute; left: 728px; top: 94px;
    font-size: 34px; font-weight: 300; color: var(--ink-soft);
    line-height: 1; white-space: nowrap;
  }
  .brand {
    position: absolute; left: 60px; top: 300px; width: 446px;
    text-align: center;
  }
  .brand__mark {
    font-size: 132px; font-weight: 600; line-height: 1;
    letter-spacing: -2px; color: var(--ink);
  }
  .brand__name {
    margin-top: 18px;
    font-size: 22px; font-weight: 400; letter-spacing: 0.2px;
    text-transform: uppercase; white-space: nowrap; color: var(--ink);
  }
  .divider {
    position: absolute; left: 553px; top: 250px;
    width: 3px; height: 345px; background: var(--ink);
  }
  .contact {
    position: absolute; left: 560px; top: 266px; width: 400px;
    text-align: center; font-size: 21px; font-weight: 300; color: var(--ink);
  }
  .contact__item { margin-bottom: 26px; }
  .contact__icon { display: block; margin: 0 auto 8px; width: 26px; height: 26px; }
  .contact__line { line-height: 35px; white-space: nowrap; }
</style>
</head>
<body>
  <article class="card">
    <h1 class="card__name">Owen R Pelley</h1>
    <p class="card__title">Vice President</p>

    <div class="brand">
      <div class="brand__mark">BLS</div>
      <div class="brand__name">Bramford Ledger Services</div>
    </div>

    <div class="divider"></div>

    <div class="contact">
      <div class="contact__item">
        <svg class="contact__icon" viewBox="0 0 26 26" aria-hidden="true">
          <circle cx="13" cy="13" r="13" fill="var(--ink)"/>
          <path d="M9 7.5c.6-.5 1.4-.4 1.8.2l1.2 1.9c.3.5.2 1.1-.2 1.5l-.8.7c.6 1.4 1.7 2.6 3.1 3.3l.7-.8c.4-.4 1-.5 1.5-.2l1.9 1.2c.6.4.7 1.2.2 1.8l-.9 1c-.7.7-1.8.9-2.7.5-3.2-1.4-5.7-3.9-7.1-7.1-.4-.9-.2-2 .5-2.7z" fill="#fff"/>
        </svg>
        <div class="contact__line">owen@bramfordls.net</div>
      </div>
      <div class="contact__item">
        <svg class="contact__icon" viewBox="0 0 26 26" aria-hidden="true">
          <circle cx="13" cy="13" r="13" fill="var(--ink)"/>
          <rect x="7" y="8.5" width="12" height="9" rx="1" fill="#fff"/>
          <path d="M7.5 9.2 13 13.6l5.5-4.4M7.5 17l4-3.6M18.5 17l-4-3.6" fill="none" stroke="var(--ink)" stroke-width="1.2"/>
        </svg>
        <div class="contact__line">702-555-0147</div>
      </div>
      <div class="contact__item">
        <svg class="contact__icon" viewBox="0 0 26 26" aria-hidden="true">
          <circle cx="13" cy="13" r="13" fill="var(--ink)"/>
          <path d="M13 6.5 6.5 12.5h2v6.5h3.5v-4h2v4h3.5v-6.5h2z" fill="#fff"/>
        </svg>
        <div class="contact__line">742 Quarry Ridge Road Suite 310</div>
        <div class="contact__line">Las Vegas, NV 89135</div>
      </div>
    </div>
  </article>
</body>
</html>
```